Harrowgate Estates Business Card for Apartment Buildings

Create business cards for resident managers who run apartment buildings. The audience is the public who are searching for apartment rentals, and current residents who live at the apartment building. Key design element will be incorporating the company logo, however, the logo cannot dominate. The building name and manager name are more important than the logo. Current business card design leaves little room for copy, so we may need to reduce the size on the current card to allow for more space for copy.

Target Market(s)

Adults 18-65 years of age, who are looking for an apartment rental, plus current residents who live at our apartment buildings.

Industry/Entity Type

Property Management

Contact Information for Business Card

A major design element will be use of the company logo. Important property and manager contact information must be part of the design. The size of the logo will need to be reduced to make room for building and manager contact copy.

Font styles to use
Sans Serif

Colors
3176b5
000000
959595
ffffff

Requirements
Must have
• 1) Incorporate the company logo.
• 2) Use the company colors (dark blue, black/grey, over white).
• 3) FEATURE THE BUILDING NAME
• 4) FEATURE THE MANAGER NAME
• 5) The company name is less important than BUILDING and MANAGER
• 6) Manager contact information
• **SEE ATTACHED CREATIVE BRIEF**
Nice to have
• 1) Back of card logo watermark
• 2) Ability to write notes on back of carfd
Should not have
• Avoid letting the company logo dominate the card, the building name and manager are more important than the company logo.

```html
<!DOCTYPE html>
<html lang="en">
<head>
<meta charset="utf-8">
<title>Harrowgate Estates – Resident Manager Business Card</title>
<link rel="stylesheet" href="https://fonts.googleapis.com/css2?family=Roboto+Condensed:wght@700&family=Oswald:wght@600&family=Montserrat:wght@600;700&family=Roboto:wght@500&display=swap">
<style>
  :root {
    --backdrop: #2d2e30;
    --brand-blue: #0e6aa6;
    --deep-blue: #1f5f8b;
    --ink: #3f4043;
    --sky: #9dbfd6;
    --band: #b8d4e6;
    --rule: #2f78ad;
    --paper: #ffffff;
    --grey-light: #e9e9e9;
    --grey-mid: #c4c4c4;
  }
  * { margin: 0; padding: 0; box-sizing: border-box; }
  html, body { width: 1200px; height: 1200px; overflow: hidden; background: var(--backdrop); }
  .canvas { position: relative; width: 1200px; height: 1200px; }
  .card { position: absolute; left: 210px; width: 850px; height: 491px; overflow: hidden; background: var(--paper); }
  .card--front { top: 109px; }
  .card--back { top: 651px; background: linear-gradient(160deg, #fbfbfb 0%, #f0f0f0 55%, #dcdcdc 100%); }
  .card__art { position: absolute; inset: 0; }

  .building-name {
    position: absolute; left: 226px; top: 18px; width: 490px; text-align: center;
    font: 700 36px/1 "Roboto Condensed", sans-serif; color: var(--deep-blue); letter-spacing: 0.2px;
  }
  .address {
    position: absolute; left: 300px; top: 64px; width: 400px; text-align: center;
    font: 700 18px/25px "Montserrat", sans-serif; color: var(--ink); letter-spacing: 1.6px;
  }
  .manager-name {
    position: absolute; left: 300px; top: 136px; width: 420px; text-align: center;
    font: 600 50px/1 "Oswald", sans-serif; color: var(--brand-blue); letter-spacing: -0.5px;
  }
  .manager-title {
    position: absolute; left: 300px; top: 197px; width: 420px; text-align: center;
    font: 500 21px/1 "Roboto", sans-serif; color: var(--ink); letter-spacing: 0.4px;
  }
  .contact-list { position: absolute; left: 432px; top: 350px; list-style: none; }
  .contact-list li { display: flex; align-items: center; height: 25px; }
  .contact-list li + li { margin-top: 1px; }
  .contact-list li:nth-child(3) { margin-top: 4px; }
  .contact-list svg { width: 34px; height: 20px; margin-right: 27px; fill: var(--ink); }
  .contact-list span { font: 700 17px/1 "Montserrat", sans-serif; color: var(--ink); letter-spacing: 2px; }
  .contact-list li:last-child span { letter-spacing: 0.8px; }

  .front-mark {
    position: absolute; left: 40px; top: 330px; display: flex; align-items: center; gap: 12px;
    font: 700 22px/1.15 "Montserrat", sans-serif; color: var(--brand-blue);
  }
  .front-mark .dot, .back-mark .dot { width: 22px; height: 22px; border-radius: 50%; background: var(--brand-blue); flex: none; }

  .back-columns {
    position: absolute; left: 0; top: 0; width: 168px; height: 491px;
    background: linear-gradient(90deg, #c9c9c9 0%, #e6e6e6 40%, #cfcfcf 70%, #ececec 100%);
  }
  .back-mark {
    position: absolute; left: 250px; top: 56px; display: flex; align-items: center; gap: 14px;
    font: 700 34px/1 "Montserrat", sans-serif; color: var(--brand-blue); letter-spacing: 0.5px;
  }
  .notes {
    position: absolute; left: 60px; top: 149px; width: 736px; height: 302px;
    background: var(--paper); border: 2px solid #bdbdbd;
  }
  .notes__line { position: absolute; left: 12px; right: 12px; height: 2px; background: var(--rule); }
</style>
</head>
<body>
<main class="canvas">

  <section class="card card--front" aria-label="Business card front">
    <svg class="card__art" viewBox="0 0 850 491" aria-hidden="true">
      <defs>
        <linearGradient id="panel-top" x1="0" y1="0" x2="0" y2="1">
          <stop offset="0" stop-color="#9dbfd6"/>
          <stop offset="0.55" stop-color="#c5dbe9"/>
          <stop offset="1" stop-color="#ffffff"/>
        </linearGradient>
        <linearGradient id="panel-bottom" x1="0" y1="0" x2="0" y2="1">
          <stop offset="0" stop-color="#ffffff"/>
          <stop offset="0.45" stop-color="#c5dbe9"/>
          <stop offset="1" stop-color="#9dbfd6"/>
        </linearGradient>
      </defs>
      <polygon points="191,0 850,0 850,256 323,256" fill="url(#panel-top)"/>
      <polygon points="332,273 850,273 850,491 443,491" fill="url(#panel-bottom)"/>
      <rect x="323" y="256" width="527" height="17" fill="var(--band)"/>
    </svg>

    <h1 class="building-name">LINDEN COURT APARTMENTS</h1>
    <p class="address">2845 Larkspur Avenue<br>Riverton, CA 95501</p>
    <h2 class="manager-name">Marisol Delgado</h2>
    <p class="manager-title">Resident Manager</p>

    <ul class="contact-list">
      <li>
        <svg viewBox="0 0 34 20" aria-label="Office phone"><path d="M2 7c0-4 30-4 30 0v3h-7V7H9v3H2z"/><rect x="7" y="10" width="20" height="9" rx="2"/></svg>
        <span>555-210-4381</span>
      </li>
      <li>
        <svg viewBox="0 0 34 20" aria-label="Fax"><rect x="11" y="1" width="14" height="7" fill="none" stroke="var(--ink)" stroke-width="1.6"/><rect x="3" y="8" width="30" height="11" rx="2" fill="none" stroke="var(--ink)" stroke-width="1.6"/><rect x="1" y="10" width="5" height="8" fill="none" stroke="var(--ink)" stroke-width="1.4"/></svg>
        <span>555-210-4390</span>
      </li>
      <li>
        <svg viewBox="0 0 34 20" aria-label="Mobile"><rect x="2" y="0" width="32" height="20" rx="4"/><path d="M13 4c-2 1-2 4 1 8s6 5 8 4l1-2-3-2-1 1c-2-1-3-3-4-5l1-1-1-3z" fill="#fff"/></svg>
        <span>555-630-7742</span>
      </li>
      <li>
        <svg viewBox="0 0 34 20" aria-label="Email"><rect x="2" y="2" width="30" height="16" fill="none" stroke="var(--ink)" stroke-width="1.4"/><path d="M2 2l15 10 15-10M2 18l11-8M32 18l-11-8" fill="none" stroke="var(--ink)" stroke-width="1.2"/></svg>
        <span>marisol@harrowgateest.com</span>
      </li>
    </ul>

    <div class="front-mark"><span class="dot"></span><span>Harrowgate<br>Estates</span></div>
  </section>

  <section class="card card--back" aria-label="Business card back">
    <div class="back-columns" role="img" aria-label="Decorative architectural columns in soft grey tones"></div>
    <div class="back-mark"><span class="dot"></span><span>HARROWGATE ESTATES LLC</span></div>
    <div class="notes" aria-label="Space for notes">
      <div class="notes__line" style="top:42px"></div>
      <div class="notes__line" style="top:85px"></div>
      <div class="notes__line" style="top:131px"></div>
      <div class="notes__line" style="top:178px"></div>
      <div class="notes__line" style="top:223px"></div>
      <div class="notes__line" style="top:269px"></div>
    </div>
  </section>

</main>
</body>
</html>
```